Wedding Invitation and envelope package

I need the 1st of many invitation designs. This is a floral collection and I have attached many designs that I like from competitors. I think that the pastel look is the best but I am hoping you can make something special. The font selection is just as important as the imagery. The overall size with bleeds is 5.25 x 7.25" and I have attached a sample to make sure sizing is clear. I also need A7 envelopes to go with the invitation, front and back flap. I want someone to look at the design and say they would pick it over any of the samples. I will need 8 total floral designs done over the next few weeks after this 1st one is done. I will also need a collection of 8 modern designs done. Please ask any questions

Font styles to use
Serif
Sans Serif
Script

Requirements
Must have
• This is a single sided invitation, a back side is not needed.
Should not have
• No full solid dark backgrounds

```html
<!DOCTYPE html>
<html lang="en">
<head>
<meta charset="utf-8">
<title>Wedding Invitation – Harriet &amp; Thomas</title>
<link href="https://fonts.googleapis.com/css2?family=Cormorant+Garamond:wght@400;500&family=Great+Vibes&display=swap" rel="stylesheet">
<style>
  :root {
    --bg-top: #ead9d0;
    --bg-mid: #f1e4d6;
    --bg-glow: #fbf2c4;
    --ink-script: #9b6a68;
    --ink-caps: #a27168;
    --ring-gold: #d8a474;
    --disc: #ffffff;
    --bloom-rose: #e6949a;
    --bloom-peach: #f1b48e;
    --bloom-coral: #e98a6e;
    --bloom-leaf: #b7c6a6;
    --bloom-blush: #f2c2bd;
  }
  * { margin: 0; padding: 0; box-sizing: border-box; }
  html, body { width: 857px; height: 1200px; overflow: hidden; }
  body { background: var(--bg-top); }

  .invitation {
    position: relative;
    width: 857px;
    height: 1200px;
    overflow: hidden;
    background:
      radial-gradient(ellipse 520px 460px at 50% 86%, var(--bg-glow) 0%, rgba(251,242,196,0) 78%),
      linear-gradient(180deg, var(--bg-top) 0%, var(--bg-mid) 55%, #f5ecd2 100%);
    font-family: "Cormorant Garamond", Georgia, serif;
    font-variant-numeric: lining-nums;
    color: var(--ink-caps);
    text-align: center;
  }

  .floral-wreath {
    position: absolute;
    left: 106px;
    top: -35px;
    width: 680px;
    height: 680px;
    border-radius: 50%;
    background: conic-gradient(from -20deg,
      var(--bloom-blush), var(--bloom-rose) 12%, var(--bloom-peach) 24%,
      var(--bloom-rose) 36%, var(--bloom-peach) 46%, var(--bloom-rose) 56%,
      var(--bloom-coral) 66%, var(--bloom-rose) 76%, var(--bloom-leaf) 86%,
      var(--bloom-blush) 100%);
    -webkit-mask: radial-gradient(circle at 50% 50%, transparent 205px, #000 235px, #000 300px, transparent 340px);
            mask: radial-gradient(circle at 50% 50%, transparent 205px, #000 235px, #000 300px, transparent 340px);
    opacity: 0.85;
  }

  .name-disc {
    position: absolute;
    left: 221px;
    top: 80px;
    width: 450px;
    height: 450px;
    border-radius: 50%;
    background: var(--disc);
    border: 4px solid var(--ring-gold);
    box-shadow: 0 0 0 8px rgba(255,255,255,0.5);
    display: flex;
    justify-content: center;
    align-items: center;
  }
  .couple-names {
    font-family: "Great Vibes", cursive;
    font-weight: 400;
    font-size: 64px;
    line-height: 70px;
    color: var(--ink-script);
  }

  .details {
    position: absolute;
    left: 0;
    right: 0;
    top: 650px;
  }
  .caps {
    font-size: 23px;
    letter-spacing: 1.5px;
    line-height: 38px;
    text-transform: uppercase;
    font-weight: 500;
  }
  .host-names {
    font-family: "Great Vibes", cursive;
    font-size: 56px;
    line-height: 70px;
    color: var(--ink-script);
    margin: 2px 0 2px;
  }
  .event-date { margin-top: 6px; }
  .venue { margin-top: 6px; }
  .rsvp { margin-top: 16px; font-size: 21px; }
</style>
</head>
<body>
  <main class="invitation">
    <div class="floral-wreath" role="img" aria-label="Watercolour wreath of pink, peach and coral roses with soft green leaves"></div>

    <div class="name-disc">
      <h1 class="couple-names">Harriet<br>Ellison<br>&amp;<br>Thomas<br>Whitley</h1>
    </div>

    <section class="details">
      <p class="caps">Request the company of</p>
      <p class="host-names">Clara &amp; Oliver</p>
      <p class="caps">To join them in<br>celebration of their marriage<br>at an evening reception on</p>
      <p class="caps event-date">Saturday 1st July, 2021<br>7.30pm</p>
      <p class="caps venue">At Ashby Hall, Ashby Green,<br>Millbrook Lane, Dorset<br>DT9 4QX</p>
      <p class="caps rsvp">RSVP by 1 March 2021</p>
    </section>
  </main>
</body>
</html>
```